Looking for awesome business card design with attached existing logo

We are a water, mold, and fire damage restoration company called "Torvane Seco" Looking for an awesome business card that is edgy yet professional and unique. Show me what you got!

```html
<!DOCTYPE html>
<html lang="en">
<head>
<meta charset="utf-8">
<title>Torvane Seco — Business Card</title>
<link rel="stylesheet" href="https://fonts.googleapis.com/css2?family=Montserrat:wght@400;500;700;800&display=swap">
<style>
  :root {
    --teal: #2d4b58;
    --gold: #d4972a;
    --white: #ffffff;
    --ink: #1f2a30;
    --backdrop: #b9b9b9;
  }
  * { box-sizing: border-box; margin: 0; padding: 0; }
  html, body { width: 1200px; height: 856px; overflow: hidden; }
  body {
    background: var(--backdrop);
    font-family: "Montserrat", sans-serif;
    display: flex;
    align-items: center;
    justify-content: center;
    gap: 40px;
  }
  .card {
    position: relative;
    width: 540px;
    height: 308px;
    overflow: hidden;
    box-shadow: 0 10px 30px rgba(0,0,0,0.25);
  }

  /* Front */
  .card-front { background: var(--white); }
  .front-brand {
    position: absolute;
    left: 34px;
    top: 96px;
    width: 180px;
    display: flex;
    align-items: center;
    gap: 10px;
  }
  .brand-dot {
    width: 14px; height: 14px;
    border-radius: 50%;
    background: var(--gold);
    flex: none;
  }
  .front-brand .brand-name {
    font-weight: 800;
    font-size: 24px;
    line-height: 1.05;
    color: var(--teal);
    letter-spacing: 0.5px;
  }
  .divider {
    position: absolute;
    left: 232px;
    top: 70px;
    width: 1px;
    height: 112px;
    background: var(--gold);
  }
  .contact {
    position: absolute;
    left: 256px;
    top: 44px;
  }
  .person-name {
    font-weight: 800;
    font-size: 19px;
    color: var(--teal);
    text-transform: uppercase;
    letter-spacing: 0.3px;
  }
  .person-name .surname { color: var(--gold); }
  .person-role {
    font-size: 12.5px;
    color: var(--ink);
    margin-top: 2px;
  }
  .contact-list {
    list-style: none;
    margin-top: 14px;
  }
  .contact-list li {
    display: flex;
    align-items: center;
    gap: 9px;
    font-size: 12.5px;
    color: var(--ink);
    margin-bottom: 6px;
  }
  .contact-icon { width: 14px; height: 14px; flex: none; }
  .address-band {
    position: absolute;
    left: 0;
    bottom: 22px;
    width: 88%;
    height: 40px;
    background: var(--teal);
    color: var(--white);
    font-size: 13px;
    font-weight: 500;
    display: flex;
    align-items: center;
    padding-left: 34px;
    letter-spacing: 0.2px;
  }
  .corner-block {
    position: absolute;
    right: 0;
    bottom: 70px;
    width: 44px;
    height: 46px;
    background: var(--gold);
  }

  /* Back */
  .card-back {
    background: var(--teal);
    display: flex;
    align-items: center;
    justify-content: center;
    gap: 14px;
  }
  .card-back .brand-dot { width: 20px; height: 20px; }
  .card-back .brand-name {
    font-weight: 800;
    font-size: 44px;
    color: var(--white);
    letter-spacing: 1px;
  }
</style>
</head>
<body>
  <section class="card card-front" aria-label="Business card front">
    <div class="front-brand">
      <span class="brand-dot"></span>
      <span class="brand-name">Torvane Seco</span>
    </div>
    <div class="divider"></div>
    <div class="contact">
      <h1 class="person-name">Delan <span class="surname">Orwick</span></h1>
      <p class="person-role">Managing Director</p>
      <ul class="contact-list">
        <li>
          <svg class="contact-icon" viewBox="0 0 16 16" aria-hidden="true"><circle cx="8" cy="8" r="8" fill="#d4972a"/><path d="M5 4.2c.4-.3.9-.3 1.1.1l.8 1.4c.2.4.1.8-.2 1l-.5.4c.4.9 1.1 1.7 2 2.2l.5-.4c.3-.3.7-.3 1 0l1.3.9c.4.2.4.8.1 1.1l-.6.6c-.6.5-1.5.5-2.3.1C6.5 10.5 5 8.9 4.3 7c-.3-.9-.1-1.9.7-2.8z" fill="#fff"/></svg>
          555-204-7781
        </li>
        <li>
          <svg class="contact-icon" viewBox="0 0 16 16" aria-hidden="true"><circle cx="8" cy="8" r="8" fill="#d4972a"/><rect x="4" y="5.2" width="8" height="5.6" rx="0.6" fill="#fff"/><path d="M4.2 5.6 8 8.5l3.8-2.9" stroke="#d4972a" stroke-width="0.9" fill="none"/></svg>
          info@torvaneseco.com-au
        </li>
        <li>
          <svg class="contact-icon" viewBox="0 0 16 16" aria-hidden="true"><circle cx="8" cy="8" r="8" fill="#d4972a"/><circle cx="8" cy="8" r="4" fill="none" stroke="#fff" stroke-width="1"/><ellipse cx="8" cy="8" rx="1.7" ry="4" fill="none" stroke="#fff" stroke-width="0.9"/><path d="M4 8h8" stroke="#fff" stroke-width="0.9"/></svg>
          www.torvaneseco.com-au
        </li>
      </ul>
    </div>
    <div class="corner-block"></div>
    <div class="address-band">4187 Calder Avenue Westbrook, QC, H2R4M7</div>
  </section>

  <section class="card card-back" aria-label="Business card back">
    <span class="brand-dot"></span>
    <span class="brand-name">Torvane Seco</span>
  </section>
</body>
</html>
```